Locksmith Business Cards

My father-in-law is in need of new business cards for his locksmith business and I need to impress him. Kindly help me out!

You can see the previous business card attached. It is a family run business in North Wales.

No individual names on the cards.

Key Things to Feature:
- The words "Prompt", "Local", "Reliable" (as you can see under the logo on the website)
- 24h Emergency Service
- Covering All of North Wales, the Wirral and Chester
- The color blue
- A key or a lock would be interesting (similar to the ones that come up when you google locksmith business card)

Optional (only if design includes bullet points, like the example below):
https://imgvaultcdnx.net/design_img/318264/57190/57190_2749031_318264_image.jpg
- Residential / Commercial / Automotive
- Alarms & Cameras
- Key Cutting & Safes

https://www.bryncoed-locksmiths-demo.co.uk/

Locksmith

01632 960 418
07700 900 362
bryncoedlocksmiths@mailvalex.com
Bryncoed Locksmiths, Hafod Barn, 4 Pennant Rd., Llandudno LL39 7QZ
www.bryncoed-locksmiths-demo.co.uk

• - The words "Prompt", "Local", "Reliable" (as you can see under the logo on the website)
• - 24h Emergency Service
• - Covering All of North Wales, the Wirral and Chester
• - A key or a lock would be interesting (similar to the ones that come up when you google locksmith business card)

```html
<!DOCTYPE html>
<html lang="en">
<head>
<meta charset="utf-8">
<title>Bryncoed Locksmiths – Business Card</title>
<link rel="stylesheet" href="https://fonts.googleapis.com/css2?family=Tinos&family=Arimo&display=swap">
<style>
  :root {
    --bg: #dcdee1;
    --blue: #2d6aff;
    --navy: #001b9b;
    --paper: #f5fdff;
    --address-light: #4f86ff;
  }
  html, body { margin: 0; padding: 0; width: 1200px; height: 1200px; overflow: hidden; background: var(--bg); }
  .card { position: absolute; left: 180px; width: 840px; height: 478px; border-radius: 14px; overflow: hidden; }
  .card--front { top: 98px; background: var(--blue); }
  .card--back { top: 622px; background: var(--paper); }

  .header-band { position: absolute; left: 0; top: 27px; width: 840px; height: 87px; background: var(--navy); }
  .header-logo-area { position: absolute; left: 0; top: 27px; width: 410px; height: 87px; background: var(--paper);
    clip-path: polygon(0 0, 100% 0, 88.3% 100%, 0 100%); }

  .brand { position: absolute; display: flex; align-items: center; gap: 12px; }
  .brand__dot { flex: none; background: var(--navy); border-radius: 50%; }
  .brand__name { font-family: 'Tinos', serif; font-weight: 400; color: var(--navy); white-space: nowrap; line-height: 1; }
  .brand--front { left: 30px; top: 27px; height: 87px; }
  .brand--front .brand__dot { width: 34px; height: 34px; }
  .brand--front .brand__name { font-size: 29px; }
  .brand--back { left: 0; width: 840px; justify-content: center; top: 212px; gap: 16px; }
  .brand--back .brand__dot { width: 46px; height: 46px; }
  .brand--back .brand__name { font-size: 44px; }

  .tagline { position: absolute; left: 412px; top: 52px; width: 410px; display: flex; justify-content: space-between;
    font-family: 'Tinos', serif; font-size: 31px; color: var(--paper); }

  .service { position: absolute; left: 30px; margin: 0; font-family: 'Tinos', serif; font-size: 26px; color: var(--paper); }
  .service--hours { top: 128px; }
  .service--area { top: 171px; }

  .key-illustration { position: absolute; left: 30px; top: 237px; width: 168px; height: 81px; border-radius: 40px 12px 12px 40px;
    background: linear-gradient(90deg, #f5fdff, #dbe7ff); }

  .divider { position: absolute; left: 0; top: 342px; width: 840px; height: 20px; background: var(--navy); }

  .contact { position: absolute; display: flex; align-items: center; gap: 14px; font-family: 'Arimo', sans-serif; font-size: 25px; color: var(--paper); }
  .contact svg { flex: none; }
  .contact--web { left: 30px; top: 366px; }
  .contact--mail { left: 30px; top: 414px; }
  .contact--phone1 { left: 556px; top: 366px; }
  .contact--phone2 { left: 556px; top: 414px; }

  .footer-band { position: absolute; left: 0; bottom: 0; width: 840px; height: 22px; background: var(--navy); }
  .address { position: absolute; left: 0; width: 840px; text-align: center; font-family: 'Tinos', serif; font-size: 20px; margin: 0; }
  .address--front { top: 456px; line-height: 22px; color: var(--address-light); }
  .address--back { top: 410px; color: var(--navy); }
</style>
</head>
<body>
  <section class="card card--front">
    <div class="header-band"></div>
    <div class="header-logo-area"></div>
    <div class="brand brand--front">
      <span class="brand__dot"></span>
      <span class="brand__name">Bryncoed Locksmiths</span>
    </div>
    <div class="tagline"><span>PROMPT</span><span>LOCAL</span><span>RELIABLE</span></div>

    <p class="service service--hours">24h Emergency Service</p>
    <p class="service service--area">Covering All of North Wales, the Wirral and Chester</p>

    <div class="key-illustration" role="img" aria-label="White key illustration"></div>

    <div class="divider"></div>

    <div class="contact contact--web">
      <svg width="26" height="26" viewBox="0 0 26 26" fill="none" stroke="#f5fdff" stroke-width="1.8">
        <circle cx="13" cy="13" r="11.5"/><ellipse cx="13" cy="13" rx="5" ry="11.5"/><path d="M1.5 13h23M3.5 7h19M3.5 19h19"/>
      </svg>
      <span>www.bryncoed-locksmiths-demo.co.uk</span>
    </div>
    <div class="contact contact--mail">
      <svg width="28" height="22" viewBox="0 0 28 22" fill="none" stroke="#f5fdff" stroke-width="1.8">
        <rect x="1" y="1" width="26" height="20" rx="2"/><path d="M1 2l13 11L27 2M1 21l10-9M27 21l-10-9"/>
      </svg>
      <span>bryncoedlocksmiths@mailvalex.com</span>
    </div>
    <div class="contact contact--phone1">
      <svg width="26" height="26" viewBox="0 0 26 26">
        <circle cx="13" cy="13" r="13" fill="#f5fdff"/>
        <path d="M8 6.5c1-.6 1.8 0 2.4 1l1.2 2.2c.4.8.1 1.4-.6 1.9l-.8.6c.8 1.9 2 3.2 3.900 4.1l.6-.8c.5-.7 1.2-.9 1.9-.5l2.2 1.2c.9.5 1.4 1.4.8 2.3-.9 1.4-2.4 2.3-4.2 1.8-4.1-1.2-7.4-4.5-8.5-8.6-.4-1.6.2-3.3 1.1-4.2z" fill="#2d6aff"/>
      </svg>
      <span>01632 960 418</span>
    </div>
    <div class="contact contact--phone2">
      <svg width="26" height="26" viewBox="0 0 26 26">
        <circle cx="13" cy="13" r="13" fill="#f5fdff"/>
        <path d="M8 6.5c1-.6 1.8 0 2.4 1l1.2 2.2c.4.8.1 1.4-.6 1.9l-.8.6c.8 1.9 2 3.2 3.9 4.1l.6-.8c.5-.7 1.2-.9 1.9-.5l2.2 1.2c.9.5 1.4 1.4.8 2.3-.9 1.4-2.4 2.3-4.2 1.8-4.1-1.2-7.4-4.5-8.5-8.6-.4-1.6.2-3.3 1.1-4.2z" fill="#2d6aff"/>
      </svg>
      <span>07700 900 362</span>
    </div>

    <div class="footer-band"></div>
    <p class="address address--front">Bryncoed Locksmiths, Hafod Barn, 4 Pennant Rd., Llandudno LL39 7QZ</p>
  </section>

  <section class="card card--back">
    <div class="brand brand--back">
      <span class="brand__dot"></span>
      <span class="brand__name">Bryncoed Locksmiths</span>
    </div>
    <p class="address address--back">Bryncoed Locksmiths, Hafod Barn, 4 Pennant Rd., Llandudno LL39 7QZ</p>
    <div class="footer-band"></div>
  </section>
</body>
</html>
```